Business Card for New Business

Please design a business card using our logo and font files. This is only one card for one person, as listed in details section.

Industry/Entity Type

Business

Contact Information for Business Card

Carl Voserby

Phone 240.318.6624
Cell 703.581.4096
Email carl@moltravex.com

www.moltravex.com

Address
18250 Brennick Lane #314
Damascus, MD 20715

Font styles to use
Sans Serif

Requirements
Must have
• Information listed in detail section. Must be standard card size.

```html
<!DOCTYPE html>
<html lang="en">
<head>
<meta charset="utf-8">
<title>Business Card – Carl Voserby</title>
<link rel="stylesheet" href="https://fonts.googleapis.com/css2?family=Quicksand:wght@400;700&display=swap">
<style>
  :root {
    --backdrop: #2a2a2a;
    --card-white: #ffffff;
    --facet-grey: #eceef0;
    --band-dark: #2f2927;
    --accent-orange: #cc5f18;
    --accent-orange-deep: #a84c12;
    --logo-rust: #b5421a;
    --text-light: #ffffff;
  }
  html, body {
    margin: 0;
    width: 1200px;
    height: 1200px;
    overflow: hidden;
    background: var(--backdrop);
    font-family: "Quicksand", sans-serif;
  }
  .business-card {
    position: absolute;
    left: 75px;
    top: 300px;
    width: 1050px;
    height: 600px;
    background: var(--card-white);
    overflow: hidden;
  }
  .card-shapes {
    position: absolute;
    inset: 0;
  }
  .brand {
    position: absolute;
    top: 120px;
    left: 0;
    right: 0;
    display: flex;
    justify-content: center;
    align-items: center;
    gap: 22px;
  }
  .brand-dot {
    width: 46px;
    height: 46px;
    border-radius: 50%;
    background: var(--logo-rust);
  }
  .brand-name {
    font-size: 68px;
    font-weight: 400;
    color: var(--logo-rust);
    letter-spacing: 1px;
  }
  .person-name {
    position: absolute;
    top: 322px;
    left: 300px;
    width: 450px;
    text-align: center;
    font-size: 50px;
    color: var(--text-light);
    font-weight: 400;
  }
  .person-name .first { font-weight: 700; }
  .contact {
    position: absolute;
    color: var(--text-light);
    font-size: 27px;
    line-height: 1.15;
    font-weight: 400;
  }
  .contact-phone { left: 215px; top: 442px; display: flex; gap: 18px; align-items: center; }
  .contact-web { left: 530px; top: 442px; display: flex; gap: 16px; align-items: center; }
  .contact-web .lines { font-size: 24px; }
  .contact-address { left: 0; right: 0; top: 528px; text-align: center; font-size: 31px; }
</style>
</head>
<body>
  <div class="business-card">
    <svg class="card-shapes" width="1050" height="600" viewBox="0 0 1050 600" aria-hidden="true">
      <polygon points="0,0 260,0 360,370 0,370" fill="var(--facet-grey)"/>
      <polygon points="1050,0 880,0 700,370 1050,370" fill="var(--facet-grey)"/>
      <polygon points="330,0 720,0 690,370 360,370" fill="var(--card-white)"/>
      <rect x="0" y="360" width="1050" height="240" fill="var(--band-dark)"/>
      <rect x="0" y="354" width="1050" height="7" fill="var(--accent-orange)"/>
      <polygon points="235,360 300,312 300,420" fill="var(--accent-orange-deep)"/>
      <polygon points="815,360 750,312 750,420" fill="var(--accent-orange-deep)"/>
      <rect x="300" y="312" width="450" height="108" fill="var(--accent-orange)"/>
    </svg>

    <div class="brand">
      <span class="brand-dot"></span>
      <span class="brand-name">Moltravex Productions</span>
    </div>

    <div class="person-name"><span class="first">Carl</span> Voserby</div>

    <div class="contact contact-phone">
      <svg width="56" height="44" viewBox="0 0 56 44" aria-label="Phone">
        <path d="M4 14 Q28 0 52 14 L48 20 L38 17 L38 12 Q28 8 18 12 L18 17 L8 20 Z" fill="#fff"/>
        <rect x="14" y="22" width="28" height="20" rx="3" fill="#fff"/>
        <g fill="var(--band-dark)">
          <rect x="20" y="26" width="4" height="3"/><rect x="26" y="26" width="4" height="3"/><rect x="32" y="26" width="4" height="3"/>
          <rect x="20" y="31" width="4" height="3"/><rect x="26" y="31" width="4" height="3"/><rect x="32" y="31" width="4" height="3"/>
        </g>
      </svg>
      <div class="lines">240.318.6624<br>703.581.4096</div>
    </div>

    <div class="contact contact-web">
      <svg width="52" height="44" viewBox="0 0 52 44" aria-label="Computer">
        <rect x="3" y="3" width="46" height="30" fill="none" stroke="#fff" stroke-width="5"/>
        <rect x="22" y="33" width="8" height="6" fill="#fff"/>
        <rect x="14" y="39" width="24" height="4" fill="#fff"/>
      </svg>
      <div class="lines">carl@moltravex.com<br>www.moltravex.com</div>
    </div>

    <div class="contact contact-address">18250 Brennick Lane #314 Damascus, MD 20715</div>
  </div>
</body>
</html>
```